Life Coach business needs a website design

I would like to get support in creating a website design. I will be starting a business as a life coach and I would like to start with something basic, but chic. It will be mainly a blog for now, but then I would like to start adding videos and hopefully podcast in the future. I took professional pictures of myself that I would like to include as a cover page. My main goal with this website is to capture the right audience by connecting with them through my mission, which is to embrace their inner greatness. I want to provide a sense of love, courage and authenticity when they open my website. I have a domain in Brickloft called :"Unfold the hidden melody". I would be happy to discuss more of the details over the phone.

Target Market(s)

Young Adults (25-35)

Number of Pages Required

4 page

Colors

Designer to choose colors to be used in the design.

Requirements
Must have
• I am looking for a similar layout and vibe to these websites: https://tessawhitcombe.net/meet-tessa/
• https://www.ninaculvane.com
• My home page will include: About, Blog, Podcast, Subscribe.. (We can add icons of snapreel, vidloom and Tackboard)
• I would like to have my name in the middle (Ondra), and include a note next to my picture "Your life is like a blank canvas and only you have the power to transform it into masterpiece. Take a chance and unfold the hidden melody" O.K.

```html
<!DOCTYPE html>
<html lang="en">
<head>
<meta charset="utf-8">
<title>Unfold the hidden melody — Life Coach</title>
<link href="https://fonts.googleapis.com/css2?family=Kaushan+Script&family=Roboto:wght@400;500;700&display=swap" rel="stylesheet">
<style>
:root{
  --accent:#f2582c;
  --ink:#1b1b1b;
  --dark:#1e1e1e;
  --text:#555555;
  --muted:#9a9a9a;
  --light:#f4f4f4;
  --white:#ffffff;
  --ghost:rgba(0,0,0,0.06);
  --ghost-dark:rgba(255,255,255,0.06);
}
*{box-sizing:border-box;margin:0;padding:0}
html,body{width:1200px;height:3876px;overflow:hidden}
body{position:relative;background:var(--white);font-family:"Roboto",Arial,sans-serif;color:var(--text)}
.abs{position:absolute}
.script{font-family:"Kaushan Script",cursive;font-weight:400}
.accent{color:var(--accent)}
.photo{position:absolute}
.btn{position:absolute;display:flex;align-items:center;justify-content:center;background:var(--accent);color:var(--white);border-radius:30px;font-size:15px;font-weight:500}

/* header */
.brand{position:absolute;left:168px;top:36px;display:flex;align-items:center;gap:10px;font-family:"Roboto",Arial,sans-serif;font-weight:500;font-size:20px;color:var(--ink);white-space:nowrap}
.brand .dot{width:12px;height:12px;border-radius:50%;background:var(--accent)}
.nav{position:absolute;top:40px;left:532px;display:flex;align-items:center;gap:40px;font-size:16px;color:var(--ink)}
.nav .active{border:1.5px solid var(--ink);border-radius:20px;padding:6px 16px}
.nav .login{background:var(--accent);color:var(--white);border-radius:20px;padding:7px 20px;display:flex;align-items:center;gap:8px}

/* hero */
.hero-photo{left:0;top:0;width:600px;height:688px;background:linear-gradient(160deg,#d9cfc8 0%,#8a5d43 45%,#f1ece8 100%)}
.hero-title{left:576px;top:210px;font-size:52px;line-height:1.35;color:var(--ink)}

/* about */
.ghost-word{position:absolute;font-family:"Kaushan Script",cursive;color:var(--ghost);white-space:nowrap}
.about-photo{left:664px;top:690px;width:536px;height:690px;background:linear-gradient(170deg,#b7a893 0%,#8c7d6c 40%,#e5c8c0 70%,#a89a88 100%)}
.about-title{left:160px;top:900px;font-size:72px;color:var(--ink)}
.about-note{left:160px;top:1020px;width:440px;font-size:15px;line-height:1.7}

/* books */
.books{left:0;top:1380px;width:1200px;height:608px;background:var(--dark)}
.books-photo{left:140px;top:1444px;width:392px;height:480px;background:linear-gradient(180deg,#bcd6e4 0%,#d4c2b4 55%,#c9a99a 100%)}
.books-kicker{left:580px;top:1478px;font-size:15px;color:#cfcfcf}
.books-title{left:580px;top:1505px;font-size:36px;color:var(--white)}
.books-copy{left:580px;top:1572px;width:480px;font-size:14px;line-height:1.8;color:#cfcfcf}
.book{position:absolute;top:1780px;width:142px;height:150px;background:linear-gradient(180deg,#f6f3ee,#d9d5cc)}

/* news */
.section-title{position:absolute;left:0;width:1200px;text-align:center;font-size:48px;color:var(--ink)}
.card{position:absolute;overflow:hidden}
.card .fill{position:absolute;inset:0}
.card .veil{position:absolute;inset:0;background:rgba(246,140,110,0.55)}
.card p{position:absolute;color:var(--white);font-family:"Kaushan Script",cursive;line-height:1.5}

/* subscribe */
.sub-input{left:376px;top:2740px;width:304px;height:48px;background:#f1f1f1;border-radius:24px;padding-left:24px;display:flex;align-items:center;font-size:14px;color:var(--muted)}
.sub-consent{left:376px;top:2806px;font-size:12px;color:var(--muted);display:flex;align-items:center;gap:10px}
.sub-consent span.box{width:14px;height:14px;border:1px solid var(--muted);display:inline-block}

/* contact */
.contact{left:0;top:2880px;width:1200px;height:592px;background:var(--light)}
.contact-photo{left:640px;top:2880px;width:560px;height:592px;background:linear-gradient(160deg,#f4f4f4 0%,#9c6b4f 45%,#eceae8 100%)}
.contact-title{left:176px;top:2990px;font-size:52px;line-height:1.25;color:var(--ink)}
.contact-kicker{left:176px;top:3134px;font-size:14px;color:var(--text)}
.contact-item{position:absolute;left:200px;display:flex;align-items:center;gap:34px}
.contact-item .label{font-family:"Kaushan Script",cursive;font-size:18px;color:var(--ink)}
.contact-item .value{font-size:14px;color:var(--text)}

/* footer */
.footer{left:0;top:3472px;width:1200px;height:348px;background:var(--dark)}
.footer-brand{left:0;top:3566px;width:1200px;display:flex;justify-content:center;align-items:center;gap:12px;font-family:"Roboto",Arial,sans-serif;font-weight:500;font-size:26px;color:var(--white)}
.footer-brand .dot{width:14px;height:14px;border-radius:50%;background:var(--white)}
.footer-nav{left:0;top:3660px;width:1200px;display:flex;justify-content:center;gap:44px;font-size:15px;color:var(--white)}
.footer-social{left:0;top:3724px;width:1200px;display:flex;justify-content:center;gap:30px;font-size:14px;color:var(--white)}
.copyright{left:0;top:3820px;width:1200px;height:56px;background:var(--accent);color:var(--white);font-size:13px;display:flex;align-items:center;justify-content:center}
</style>
</head>
<body>

<!-- Hero -->
<div class="photo hero-photo" role="img" aria-label="Portrait of the life coach smiling, in a white top"></div>

<header>
  <div class="brand"><span class="dot"></span>Unfold the hidden melody</div>
  <nav class="nav">
    <span class="active">Home</span>
    <span>About</span>
    <span>Blog</span>
    <span>Podcast</span>
    <svg width="20" height="20" viewBox="0 0 20 20" aria-label="Search"><circle cx="8" cy="8" r="6" fill="none" stroke="#1b1b1b" stroke-width="2"/><line x1="12.5" y1="12.5" x2="18" y2="18" stroke="#1b1b1b" stroke-width="2"/></svg>
    <span class="login"><svg width="12" height="12" viewBox="0 0 12 12"><circle cx="6" cy="4" r="2.6" fill="#fff"/><path d="M1 12a5 5 0 0 1 10 0z" fill="#fff"/></svg>Login</span>
  </nav>
</header>

<h1 class="abs hero-title script">Uncover the <span class="accent">Secret</span> of<br><span class="accent">Successful</span> Life!</h1>
<div class="btn" style="left:580px;top:362px;width:118px;height:40px">Follow Me</div>

<!-- About -->
<div class="ghost-word" style="left:0;top:705px;font-size:200px">ABOUT</div>
<div class="photo about-photo" role="img" aria-label="The coach in a long pink dress seated on coastal rocks"></div>
<h2 class="abs about-title script">Meet <span class="accent">Ondra</span></h2>
<p class="abs about-note">Your life is like a blank canvas and only you have the power to transform it into masterpiece. Take a chance and unfold the hidden melody. — O.K.</p>
<div class="btn" style="left:160px;top:1106px;width:124px;height:42px">Read More</div>

<!-- Books -->
<div class="abs books"></div>
<div class="ghost-word" style="left:640px;top:1390px;font-size:150px;color:var(--ghost-dark)">BOOKS</div>
<div class="photo books-photo" role="img" aria-label="The coach on a beach with arms raised in a flowing dress"></div>
<div class="abs books-kicker">Books by Ondra</div>
<h2 class="abs books-title script">Read My Books &amp; Start a New Life</h2>
<p class="abs books-copy">Lorem Ipsum is simply dummy text of the printing and typesetting industry. Lorem Ipsum has been the industry's standard dummy text ever since the 1500s, when an unknown printer took a galley of type and scrambled it to make a type specimen book.</p>
<div class="book" style="left:466px" role="img" aria-label="Book cover"></div>
<div class="book" style="left:616px" role="img" aria-label="Open book spread"></div>
<div class="book" style="left:766px" role="img" aria-label="Book cover"></div>
<div class="book" style="left:916px" role="img" aria-label="Book cover"></div>

<!-- News -->
<div class="ghost-word" style="left:430px;top:1990px;font-size:130px">Blog</div>
<h2 class="section-title script" style="top:2030px">Latest <span class="accent">News</span></h2>

<div class="card" style="left:140px;top:2148px;width:452px;height:460px">
  <div class="fill" role="img" aria-label="Smiling portrait of the coach" style="background:linear-gradient(180deg,#f6b59c,#e98a6a)"></div>
  <div class="veil"></div>
  <p style="left:34px;top:260px;width:380px;font-size:28px">Neque porro quisquam est qui dolorem ipsum quia</p>
  <svg class="abs" style="left:34px;top:390px" width="70" height="20" viewBox="0 0 70 20"><line x1="0" y1="10" x2="64" y2="10" stroke="#fff" stroke-width="2.5"/><path d="M56 3l9 7-9 7" fill="none" stroke="#fff" stroke-width="2.5"/></svg>
</div>
<div class="card" style="left:612px;top:2148px;width:448px;height:220px">
  <div class="fill" role="img" aria-label="The coach posing on rocks" style="background:linear-gradient(160deg,#c99a85,#e7b8a2)"></div>
  <div class="veil"></div>
  <p style="left:30px;top:98px;width:360px;font-size:24px">Neque porro quisquam est qui dolorem ipsum quia</p>
</div>
<div class="card" style="left:612px;top:2388px;width:448px;height:220px">
  <div class="fill" role="img" aria-label="The coach posing in a pink dress" style="background:linear-gradient(160deg,#c99a85,#e7b8a2)"></div>
  <div class="veil"></div>
  <p style="left:30px;top:98px;width:360px;font-size:24px">Neque porro quisquam est qui dolorem ipsum quia</p>
</div>

<!-- Subscribe -->
<div class="ghost-word" style="left:760px;top:2650px;font-size:140px">Newsle</div>
<h2 class="section-title script" style="top:2648px;font-size:44px">Subscribe To <span class="accent">Our News!</span></h2>
<div class="abs sub-input">Email address</div>
<div class="btn" style="left:690px;top:2740px;width:130px;height:48px">Subscribe</div>
<div class="abs sub-consent"><span class="box"></span>I agree to receive updates and privacy policy</div>

<!-- Contact -->
<div class="abs contact"></div>
<div class="photo contact-photo" role="img" aria-label="Smiling portrait of the coach in a white top"></div>
<h2 class="abs contact-title script">Don't Hesitate To<br><span class="accent">Contact Me</span></h2>
<div class="abs contact-kicker">Have a Question? Contact Me Here!</div>
<div class="contact-item" style="top:3210px">
  <svg width="26" height="20" viewBox="0 0 26 20"><rect x="0" y="0" width="26" height="20" rx="2" fill="#f2582c"/><path d="M1 2l12 9 12-9" fill="none" stroke="#fff" stroke-width="2"/></svg>
  <div><div class="label">Write Me:</div><div class="value">hello@unfoldmelody.net</div></div>
</div>
<div class="contact-item" style="top:3300px">
  <svg width="26" height="26" viewBox="0 0 24 24"><path d="M6.6 10.8a15.2 15.2 0 0 0 6.6 6.6l2.2-2.2a1 1 0 0 1 1-.25 11.4 11.4 0 0 0 3.6.57 1 1 0 0 1 1 1V20a1 1 0 0 1-1 1A17 17 0 0 1 3 4a1 1 0 0 1 1-1h3.5a1 1 0 0 1 1 1 11.4 11.4 0 0 0 .57 3.6 1 1 0 0 1-.25 1z" fill="#f2582c"/></svg>
  <div><div class="label">Call Me:</div><div class="value">00-000-0000</div></div>
</div>

<!-- Footer -->
<footer>
  <div class="abs footer"></div>
  <div class="abs footer-brand"><span class="dot"></span>Unfold the hidden melody</div>
  <nav class="abs footer-nav"><span>Home</span><span>About</span><span>Blog</span><span>Podcast</span></nav>
  <div class="abs footer-social"><span>snapreel</span><span>vidloom</span><span>Tackboard</span></div>
  <div class="abs copyright">© Copyright Unfold the hidden melody</div>
</footer>

</body>
</html>
```